Fence Flyer to Attract More Sales During Winter

We need a new flyer made that we can distribute to residential mailboxes. The flyer is to promote our Frostline Picket Days. We like simply designs, and we would like the flyer to showcase a lot of our fence photos. More of our photos are online at our website at www.getbramblerail.com - our new address needs to also be featured on the flyer - 436 Quillen rd, Monroe, NC 28117. I do want the words "FROSTLINE PICKET DAYS" to be dominate on the flyer with the description "Wood fences starting at $12/FT!" Please look through our Facebook page and our website to gather more photos or information. We are flexible on colors, nothing to fancy - simple flyer design please.

Target Market(s)

Residential homeowners that need a new fence to enclose their yard for safety, security or decorative

Industry/Entity Type

Residential Construction

Font styles to use
Sans Serif

Colors

Designer to choose colors to be used in the design.

Requirements
Must have
• Frostline Picket Days
• Contact information for the business
• "Come visit our outdoor showroom, open 24/7!"
Nice to have
• Photos of our fences - you can find more on our website at www.GetBrambleRail.com or Facebook.com/MeadowlarkRailGPV
Should not have
• Flashy designs

```html
<!DOCTYPE html>
<html lang="en">
<head>
<meta charset="utf-8">
<title>Frostline Picket Days Flyer</title>
<link href="https://fonts.googleapis.com/css2?family=Roboto:ital,wght@0,400;0,700;0,900;1,400&family=Kaushan+Script&display=swap" rel="stylesheet">
<style>
  :root {
    --navy: #0b2a8c;
    --sky: #00aeef;
    --pink: #e8127e;
    --white: #ffffff;
    --wood: #c9b48a;
    --wood-dark: #8a7450;
    --leaf: #5d7a3c;
    --page: #ffffff;
  }
  * { margin: 0; padding: 0; box-sizing: border-box; }
  html, body { width: 1200px; height: 900px; overflow: hidden; background: var(--page); }
  body { font-family: "Roboto", Arial, sans-serif; color: var(--white); }

  .flyer { position: absolute; left: 310px; top: 15px; width: 611px; height: 867px; }

  .promo {
    position: absolute; left: 0; top: 0; width: 383px; height: 867px;
    background: linear-gradient(180deg, var(--navy) 0%, #0d5fc7 35%, var(--sky) 62%, var(--sky) 100%);
    overflow: hidden;
  }
  .snow { position: absolute; inset: 0; }

  .headline { position: absolute; left: 0; width: 383px; text-align: center; top: 98px; }
  .headline-script {
    font-family: "Kaushan Script", cursive; font-size: 72px; line-height: 1;
    display: block; transform: rotate(-6deg); margin-left: -14px;
  }
  .headline-main { font-weight: 700; display: block; line-height: 0.95; letter-spacing: -1px; }
  .headline-main.line-one { font-size: 62px; margin-top: 36px; }
  .headline-main.line-two { font-size: 84px; }

  .price-tag { position: absolute; left: 42px; top: 395px; width: 275px; height: 185px; }

  .call { position: absolute; left: 58px; top: 584px; width: 310px; height: 90px; }
  .call-icon { position: absolute; left: 0; top: 0; width: 40px; height: 88px; }
  .call-text { position: absolute; left: 54px; top: 2px; font-weight: 700; font-size: 33px; line-height: 42px; white-space: nowrap; }

  .address { position: absolute; left: 60px; top: 712px; font-size: 17px; display: flex; align-items: center; gap: 9px; white-space: nowrap; }
  .address svg { width: 12px; height: 17px; }

  .brand { position: absolute; left: 62px; top: 762px; display: flex; align-items: center; gap: 12px; }
  .brand-mark { width: 60px; height: 60px; background: var(--white); flex: none; }
  .brand-name { font-weight: 700; font-size: 22px; line-height: 27px; display: block; white-space: nowrap; }
  .brand-phone { font-weight: 700; font-size: 22px; line-height: 27px; display: block; }
  .brand-tagline { font-size: 9px; display: block; margin-top: 3px; white-space: nowrap; }

  .gallery { position: absolute; left: 383px; top: 0; width: 228px; height: 867px; }
  .photo { position: absolute; background: linear-gradient(180deg, #7aa05a 0%, var(--leaf) 30%, var(--wood) 55%, var(--wood-dark) 100%); }
  .photo.house { background: linear-gradient(180deg, #a8c6e8 0%, #9c6b52 30%, var(--wood) 50%, #b59e74 80%, #8a7a5c 100%); }
  .photo.shade { background: linear-gradient(180deg, #3f5a2c 0%, #c8c0a8 35%, #a99a7a 65%, #6c5a42 100%); }
  .photo.wall { background: linear-gradient(180deg, #b8cde4 0%, #e0dcd2 20%, var(--wood) 45%, #bfa882 100%); }

  .showroom-badge { position: absolute; left: 97px; top: 737px; width: 110px; height: 110px; }
</style>
</head>
<body>
<main class="flyer">
  <section class="promo">
    <svg class="snow" viewBox="0 0 383 867" aria-hidden="true">
      <g fill="#fff">
        <circle cx="52" cy="38" r="7"/><circle cx="128" cy="62" r="5"/><circle cx="211" cy="63" r="8"/>
        <circle cx="332" cy="43" r="8"/><circle cx="12" cy="111" r="5"/><circle cx="354" cy="106" r="5"/>
        <circle cx="319" cy="177" r="5"/><circle cx="67" cy="182" r="6"/><circle cx="366" cy="231" r="7"/>
        <circle cx="25" cy="242" r="7"/><circle cx="345" cy="293" r="4"/><circle cx="3" cy="325" r="4"/>
        <circle cx="262" cy="376" r="5"/><circle cx="55" cy="390" r="7"/><circle cx="155" cy="401" r="7"/>
        <circle cx="323" cy="460" r="7"/><circle cx="27" cy="530" r="5"/>
      </g>
    </svg>

    <h1 class="headline">
      <span class="headline-script">Frostline</span>
      <span class="headline-main line-one">PICKET</span>
      <span class="headline-main line-two">DAYS</span>
    </h1>

    <svg class="price-tag" viewBox="0 0 275 185" aria-label="Wood fences starting at $12 per foot">
      <g transform="rotate(-15 137 92)">
        <path d="M48 45 L262 45 L262 150 L48 150 L6 97 Z" fill="#e8127e"/>
        <circle cx="34" cy="97" r="10" fill="#00aeef"/>
        <text x="155" y="68" text-anchor="middle" font-family="Roboto, sans-serif" font-weight="700" font-size="13" fill="#fff">WOOD FENCES STARTING AT</text>
        <text x="66" y="138" font-family="Roboto, sans-serif" font-weight="400" font-size="52" fill="#fff">$</text>
        <text x="96" y="138" font-family="Roboto, sans-serif" font-weight="700" font-size="80" fill="#fff" letter-spacing="-3">12</text>
        <line x1="196" y1="134" x2="214" y2="108" stroke="#fff" stroke-width="3"/>
        <text x="212" y="140" font-family="Roboto, sans-serif" font-weight="700" font-size="12" fill="#fff">FT</text>
      </g>
    </svg>

    <div class="call">
      <svg class="call-icon" viewBox="0 0 40 88" aria-hidden="true">
        <path d="M21 2 Q29 0 33 6 L38 22 Q39 27 34 29 L27 32 Q22 34 20 31 Q15 44 20 57 Q22 54 27 56 L34 59 Q39 61 38 66 L33 82 Q29 88 21 86 Q2 79 2 44 Q2 9 21 2 Z" fill="#fff"/>
      </svg>
      <p class="call-text">CALL US NOW<br>704-555-0142</p>
    </div>

    <p class="address">
      <svg viewBox="0 0 12 17" aria-hidden="true"><path d="M6 0 A6 6 0 0 1 12 6 C12 10 6 17 6 17 C6 17 0 10 0 6 A6 6 0 0 1 6 0 Z M6 3.5 A2.5 2.5 0 1 0 6 8.5 A2.5 2.5 0 1 0 6 3.5 Z" fill="#fff" fill-rule="evenodd"/></svg>
      436 Quillen rd, Monroe, NC 28117
    </p>

    <div class="brand">
      <span class="brand-mark" aria-hidden="true"></span>
      <p>
        <span class="brand-name">Bramble Rail Fence</span>
        <span class="brand-phone">704-555-0142</span>
        <span class="brand-tagline">"Because Good Fences Make Good Neighbors"</span>
      </p>
    </div>
  </section>

  <section class="gallery">
    <div class="photo" style="left:0;top:0;width:228px;height:172px" role="img" aria-label="Photo of a wood shadowbox fence with split rail along a green lawn"></div>
    <div class="photo house" style="left:0;top:173px;width:228px;height:172px" role="img" aria-label="Photo of a new wood privacy fence beside a brick house"></div>
    <div class="photo shade" style="left:0;top:346px;width:114px;height:153px" role="img" aria-label="Photo of a wood fence line along a wooded yard"></div>
    <div class="photo" style="left:115px;top:346px;width:113px;height:153px" role="img" aria-label="Photo of a split rail fence with an arched wood gate"></div>
    <div class="photo" style="left:0;top:500px;width:114px;height:152px" role="img" aria-label="Photo of a wood fence along garden shrubs"></div>
    <div class="photo wall" style="left:115px;top:500px;width:113px;height:152px" role="img" aria-label="Photo of a scalloped wood fence beside a white house"></div>
    <div class="photo wall" style="left:0;top:653px;width:228px;height:214px" role="img" aria-label="Photo of a tall wood privacy gate beside a house"></div>

    <svg class="showroom-badge" viewBox="0 0 110 110" aria-label="Come visit our outdoor showroom, open 24/7">
      <defs><path id="badge-ring" d="M55 55 m-46 0 a46 46 0 1 1 92 0 a46 46 0 1 1 -92 0"/></defs>
      <text font-family="Roboto, sans-serif" font-weight="700" font-size="10" fill="#fff" letter-spacing="0.5">
        <textPath href="#badge-ring" startOffset="2%">COME VISIT OUR OUTDOOR SHOWROOM •</textPath>
      </text>
      <path d="M75 45 A22 22 0 1 0 75 68" fill="none" stroke="#fff" stroke-width="3"/>
      <path d="M71 40 L79 44 L73 50 Z" fill="#fff"/>
      <text x="55" y="48" text-anchor="middle" font-family="Roboto, sans-serif" font-weight="700" font-size="9" fill="#fff">OPEN</text>
      <text x="55" y="62" text-anchor="middle" font-family="Roboto, sans-serif" font-weight="700" font-size="14" fill="#fff">24</text>
      <line x1="43" y1="65" x2="67" y2="65" stroke="#fff" stroke-width="1.5"/>
      <text x="55" y="78" text-anchor="middle" font-family="Roboto, sans-serif" font-weight="700" font-size="13" fill="#fff">7</text>
    </svg>
  </section>
</main>
</body>
</html>
```